Real Estate Team Needs Business Cards

Double sided - Team Member on Front, Team Leader on Back (back side will contain more details).
Colors to use:
Red = R: 233 G: 1 B: 2
Grey = R: 89 G: 89 B: 89
Black= R: 0 B: 0 B: 0
** MAIN FOCUS ** ( separate border, color, design, etc. to really stand out - whatever you think draws the most attention ) on both sides for "Sell for 1%‡" and "Buy & receive up to a 1% rebate‡". Must have fine print **
**Please make both sides stand out and look unique / different
Business card to have round corners (standard size 3.5" x 2").:
Document Trim Size
89 x 51 mm
1050 x 600 pixels
Full Bleed Size
92 x 54 mm
1085 x 635 pixels
Basic example provided. Please redesign as you see best. In your design - Please use the same picture on both sides. Name, address, phone number, email, etc. will be provided to the selected design. QR code on back side only if there is room (not important)

```html
<!DOCTYPE html>
<html lang="en">
<head>
<meta charset="utf-8">
<title>Keystone Realty – Business Cards</title>
<link href="https://fonts.googleapis.com/css2?family=Lato:wght@400;700;900&display=swap" rel="stylesheet">
<style>
  :root {
    --red: #e90102;
    --red-light: #f0464a;
    --grey: #595959;
    --black: #000000;
    --charcoal: #262626;
    --paper: #f8f8f8;
    --stage: #e2e2e2;
    --ink: #111111;
  }
  * { margin: 0; padding: 0; box-sizing: border-box; }
  html, body { width: 1200px; height: 757px; overflow: hidden; }
  body {
    background: var(--stage);
    font-family: "Lato", Arial, sans-serif;
    color: var(--ink);
    position: relative;
  }
  .card {
    position: absolute;
    top: 289px;
    width: 490px;
    height: 292px;
    background: var(--paper);
    overflow: hidden;
  }
  .card--team { left: 79px; border-top: 6px solid var(--charcoal); }
  .card--leader { left: 618px; }

  .brand {
    position: absolute;
    display: flex;
    align-items: center;
    gap: 8px;
    font-weight: 900;
    font-size: 19px;
    letter-spacing: 0.5px;
    color: var(--black);
    white-space: nowrap;
  }
  .brand__mark { width: 14px; height: 14px; background: var(--red); }
  .card--team .brand { left: 150px; top: 46px; }
  .card--leader .brand { left: 240px; top: 52px; }

  .team-info { position: absolute; left: 28px; top: 118px; font-size: 11px; line-height: 15px; }
  .team-info__name { color: var(--red); font-weight: 700; font-size: 13px; margin-bottom: 5px; }
  .contact-line { display: flex; align-items: center; gap: 6px; margin-top: 6px; }
  .contact-line svg { width: 10px; height: 10px; flex: none; }

  .perks { position: absolute; list-style: none; font-weight: 700; font-size: 12.5px; }
  .perks li { display: flex; align-items: center; gap: 4px; height: 20px; }
  .perks svg { width: 9px; height: 9px; flex: none; }
  .card--team .perks { left: 260px; top: 116px; }
  .card--leader .perks { left: 243px; top: 114px; font-size: 12px; }
  .perks li { height: 20px; }
  .card--leader .perks li { height: 18px; }

  .skyline-band {
    position: absolute; left: 0; right: 0; top: 214px; bottom: 0;
    background: linear-gradient(180deg, #3a3a3a 0%, var(--charcoal) 40%);
  }
  .team-footer { position: absolute; left: 0; right: 0; top: 250px; text-align: center; }
  .team-footer__owner { color: #fff; font-weight: 700; font-size: 14px; }
  .team-footer__owner span { font-weight: 400; font-size: 12px; margin-left: 6px; }
  .team-footer__web { color: var(--red); font-weight: 700; font-size: 12.5px; margin-top: 2px; }

  .leader-name { position: absolute; left: 0; top: 16px; width: 166px; text-align: right; }
  .leader-name__title-name { color: var(--red); font-weight: 900; font-size: 18px; letter-spacing: 0.3px; }
  .leader-name__rule { height: 2px; background: var(--black); width: 98px; margin-top: 2px; }
  .leader-name__role { font-size: 10px; margin-top: -6px; }

  .portrait {
    position: absolute; left: 2px; top: 54px; width: 185px; height: 238px;
    background: linear-gradient(180deg, #e9e6e3 0%, #d9d3ce 45%, #24406e 75%, #1f3a66 100%);
    z-index: 2;
  }
  .red-band {
    position: absolute; left: 130px; right: 0; top: 159px; bottom: 0;
    background: linear-gradient(180deg, #ee2a2c 0%, var(--red) 25%);
  }
  .leader-contact {
    position: absolute; left: 236px; top: 202px; color: #fff; font-size: 12px; z-index: 3;
  }
  .leader-contact .contact-line { margin-top: 0; height: 21px; gap: 9px; }
  .leader-contact__web { font-weight: 700; font-size: 12.5px; margin-top: -2px; }
</style>
</head>
<body>

<section class="card card--team">
  <div class="brand"><span class="brand__mark"></span>KEYSTONE REALTY</div>

  <div class="team-info">
    <p class="team-info__name">Keystone Real Estate Team</p>
    <p>Lindenlaan 24, 4811<br>Breda The Netherlands</p>
    <p class="contact-line">
      <svg viewBox="0 0 10 10"><path fill="#e90102" d="M1 3c0-1 1-2 4-2s4 1 4 2v1H7V3H3v1H1zM2 5l1-1h4l1 1 1 4H1z"/></svg>
      555.210.4478
    </p>
    <p class="contact-line">
      <svg viewBox="0 0 10 10"><rect x="0.5" y="2" width="9" height="6.5" fill="#e90102"/><path d="M0.5 2l4.5 3.5L9.5 2" stroke="#fff" stroke-width="0.8" fill="none"/></svg>
      Contact@keystonerealty.com
    </p>
  </div>

  <ul class="perks">
    <li><svg viewBox="0 0 10 10"><path fill="#e90102" d="M0 4h5V1l5 4-5 4V6H0z"/></svg>Sell For 1%*</li>
    <li><svg viewBox="0 0 10 10"><path fill="#e90102" d="M0 4h5V1l5 4-5 4V6H0z"/></svg>Buy &amp; Recieve upto a 1% rebate*</li>
    <li><svg viewBox="0 0 10 10"><path fill="#e90102" d="M0 4h5V1l5 4-5 4V6H0z"/></svg>Free Home Evaluation</li>
    <li><svg viewBox="0 0 10 10"><path fill="#e90102" d="M0 4h5V1l5 4-5 4V6H0z"/></svg>Free local Sold Reports</li>
    <li><svg viewBox="0 0 10 10"><path fill="#e90102" d="M0 4h5V1l5 4-5 4V6H0z"/></svg>Advanced Property Search</li>
  </ul>

  <div class="skyline-band" role="img" aria-label="Dark city skyline silhouette with chevron pattern"></div>
  <div class="team-footer">
    <p class="team-footer__owner">Owner Name<span>Position</span></p>
    <p class="team-footer__web">www.KeystoneRealty.com</p>
  </div>
</section>

<section class="card card--leader">
  <div class="leader-name">
    <p class="leader-name__title-name">DANIEL HART</p>
    <div class="leader-name__rule"></div>
    <p class="leader-name__role">Broker/Owner</p>
  </div>

  <div class="brand"><span class="brand__mark"></span>KEYSTONE REALTY</div>

  <ul class="perks">
    <li><svg viewBox="0 0 10 10"><path fill="#000" d="M0 4h5V1l5 4-5 4V6H0z"/></svg>Sell For 1%*</li>
    <li><svg viewBox="0 0 10 10"><path fill="#000" d="M0 4h5V1l5 4-5 4V6H0z"/></svg>Buy &amp; Recieve upto a 1% rebate*</li>
  </ul>

  <div class="red-band" role="img" aria-label="Red city skyline silhouette with chevron pattern"></div>
  <div class="portrait" role="img" aria-label="Portrait photo of the broker in a navy suit"></div>

  <div class="leader-contact">
    <p class="contact-line">
      <svg viewBox="0 0 10 10"><path fill="#fff" d="M1 3c0-1 1-2 4-2s4 1 4 2v1H7V3H3v1H1zM2 5l1-1h4l1 1 1 4H1z"/></svg>
      555.210.4478
    </p>
    <p class="contact-line">
      <svg viewBox="0 0 10 10"><rect x="2.5" y="0.5" width="5" height="9" rx="1" fill="none" stroke="#fff"/><rect x="4.3" y="7.5" width="1.4" height="0.8" fill="#fff"/></svg>
      555.210.9036
    </p>
    <p class="contact-line">
      <svg viewBox="0 0 10 10"><rect x="0.5" y="2" width="9" height="6.5" fill="#fff"/><path d="M0.5 2l4.5 3.5L9.5 2" stroke="#e90102" stroke-width="0.8" fill="none"/></svg>
      Daniel@keystonerealty.com
    </p>
    <p class="leader-contact__web">www.KeystoneRealty.com</p>
  </div>
</section>

</body>
</html>
```